New automotive search style homepage

Looking for someone that can create a new homepage layout for my company. What we currently have is a little plain above the fold. We are an automotive technology company, where we take over the negotiation for customers, and perhaps we can have a design that appeals to that idea more. The current chat container is our only way to search currently, but would love to have a hybrid chat and manual search container, with the manual fields being make and model. This shouldn't have a toggle, but a seamless split view housing both features. You can see current design of our site at motorlane.net

Target Market(s)

Car buyers

Industry/Entity Type

Automotive

Number of Pages Required

1 page

Colors
0054AA
0677BA
7BADD7
CADEEF
E8F1F8

Requirements
Must have
• Above the fold is the most important

```html
<!DOCTYPE html>
<html lang="en">
<head>
<meta charset="utf-8">
<title>MotorLane — Car Buying, Reversed</title>
<link href="https://fonts.googleapis.com/css2?family=Inter:wght@400;500;600;700;800&display=swap" rel="stylesheet">
<style>
:root{
  --blue:#1a7fe8;
  --blue-btn:#0d6fe3;
  --navy:#0054AA;
  --deep:#0a2a66;
  --mid:#0677BA;
  --sky:#7BADD7;
  --pale:#CADEEF;
  --mist:#E8F1F8;
  --ink:#1f2937;
  --text:#4b5563;
  --muted:#8a94a3;
  --line:#e3e7ec;
  --white:#ffffff;
}
*{box-sizing:border-box;margin:0;padding:0}
html,body{width:1200px;height:3514px;overflow:hidden}
body{font-family:"Inter",Arial,sans-serif;color:var(--ink);background:var(--white);position:relative}
.abs{position:absolute}

/* nav */
.nav{position:absolute;top:0;left:0;width:1200px;height:70px;background:var(--white);border-bottom:1px solid var(--line)}
.brand{position:absolute;left:55px;top:20px;font-weight:800;font-size:27px;color:var(--blue);letter-spacing:-.5px}
.nav-links{position:absolute;left:299px;top:26px;display:flex;gap:33px;font-size:13.5px;color:#374151}
.nav-links .pro{color:var(--blue)}
.login{position:absolute;left:1045px;top:20px;width:65px;height:30px;border:1px solid var(--line);border-radius:8px;font-size:13px;color:#374151;display:flex;align-items:center;justify-content:center}
.menu{position:absolute;left:1128px;top:26px}

/* hero */
.hero{position:absolute;top:70px;left:0;width:1200px;height:650px;background:linear-gradient(100deg,#0b3a7e 0%,#0d4a97 40%,#0a2f6d 100%);overflow:hidden}
.hero-photo{position:absolute;right:0;top:0;width:700px;height:650px;background:radial-gradient(ellipse at 62% 52%,#1e7fe0 0%,#0f4fa3 32%,#08245a 62%,rgba(8,36,90,0) 100%)}
.hero h1{position:absolute;left:115px;top:118px;font-size:64px;line-height:66px;font-weight:800;color:var(--white);letter-spacing:-1px}
.hero p{position:absolute;left:115px;top:262px;font-size:25px;line-height:30px;font-weight:600;color:var(--white)}

/* split search */
.search-split{position:absolute;left:115px;top:340px;width:460px;height:104px;background:var(--white);border-radius:10px;display:flex;box-shadow:0 8px 24px rgba(0,20,60,.3)}
.chat-pane{position:relative;width:250px;padding:12px 12px;border-right:1px solid var(--line)}
.chat-text{font-size:13px;line-height:18px;font-weight:500;color:#374151}
.chat-send{position:absolute;right:10px;bottom:10px;width:28px;height:28px;border-radius:50%;background:var(--blue-btn);display:flex;align-items:center;justify-content:center}
.chat-mic{position:absolute;right:46px;bottom:16px}
.manual-pane{flex:1;padding:9px 10px;display:flex;flex-direction:column;gap:5px}
.field{height:25px;border:1px solid var(--line);border-radius:6px;background:var(--mist);font-size:12px;color:var(--text);display:flex;align-items:center;justify-content:space-between;padding:0 9px}
.go{height:26px;border-radius:6px;background:var(--blue-btn);color:var(--white);font-size:12px;font-weight:600;display:flex;align-items:center;justify-content:center}

/* section titles */
.title{position:absolute;left:0;width:1200px;text-align:center;font-size:43px;font-weight:500;color:var(--blue);letter-spacing:-.3px}

/* steps */
.step{position:absolute;left:0;width:1200px;text-align:center}
.step svg{display:block;margin:0 auto}
.step h3{font-size:24px;font-weight:500;color:#374151;margin-top:6px}
.step p{font-size:17px;color:var(--text);margin-top:8px}

.btn{position:absolute;left:497px;width:208px;height:29px;background:var(--blue-btn);color:var(--white);border-radius:15px;font-size:13.5px;font-weight:600;display:flex;align-items:center;justify-content:center}

/* deals */
.card{position:absolute;top:1584px;width:263px;height:503px;border:1px solid var(--line);border-radius:8px;overflow:hidden;background:var(--white)}
.card-photo{height:196px;background:linear-gradient(180deg,#f4f5f6 0%,#e6e8ea 70%,#c9ccd0 100%)}
.fav{position:absolute;right:10px;top:10px;width:26px;height:26px;border-radius:50%;background:#8a9099;display:flex;align-items:center;justify-content:center}
.card-body{position:absolute;left:15px;right:15px;top:212px}
.card h4{font-size:16.5px;font-weight:400;color:var(--ink)}
.trim{font-size:11px;color:var(--muted);margin-top:4px}
.price-row{display:flex;justify-content:space-between;align-items:baseline;margin-top:12px}
.price{font-size:21px;font-weight:400;color:var(--ink)}
.miles{font-size:11px;color:#374151}
.est{font-size:11px;color:var(--blue);margin-top:6px}
.tag{display:inline-block;font-size:11px;color:#9aa3ae;background:#f1f3f5;padding:3px 7px;border-radius:3px;margin-top:13px}
.swatch{font-size:11px;color:#374151;display:flex;align-items:center;gap:6px;margin-top:9px}
.dot{width:9px;height:9px;border-radius:50%;border:1px solid #9aa3ae}
.card-foot{position:absolute;left:15px;right:15px;top:455px;border-top:1px solid var(--line);padding-top:20px;font-size:11px;color:#4b5563;display:flex;align-items:center;gap:6px}

/* compare */
.compare h3{font-size:25px;font-weight:500;color:#374151}
.compare ul{list-style:none;margin-top:12px}
.compare li{font-size:18px;line-height:26.3px;color:var(--text)}
.compare li::before{content:"• "}
.compare .ours h3{color:var(--blue);font-weight:800}
.compare .ours li{font-weight:600;color:#374151}

/* faq */
.faq{position:absolute;left:229px;width:741px;border-top:2px solid #c9ced5}
.faq h4{font-size:24px;font-weight:500;color:#374151;display:flex;justify-content:space-between;align-items:center;padding-top:8px}
.faq h4 span{color:var(--blue);font-size:28px;font-weight:600}
.faq p{font-size:17px;line-height:21px;color:var(--text);margin-top:8px}
.faq-end{position:absolute;left:229px;width:741px;top:2731px;border-top:2px solid #c9ced5}

.search-pill{position:absolute;left:412px;top:2907px;width:375px;height:28px;background:var(--blue-btn);border-radius:12px;color:var(--white);font-size:13px;font-weight:600;display:flex;align-items:center;justify-content:center}

/* footer */
.footer{position:absolute;top:3006px;left:0;width:1200px;height:508px;background:linear-gradient(180deg,#0a4a9a 0%,#0c5cc0 100%);color:var(--white)}
.f-brand{position:absolute;left:53px;top:40px;font-size:40px;font-weight:800;letter-spacing:-.5px}
.f-tag{position:absolute;left:53px;top:97px;font-size:17px}
.f-contact{position:absolute;left:53px;font-size:14.5px;display:flex;align-items:center;gap:10px}
.f-col{position:absolute;top:62px;font-size:14.5px;line-height:31.5px}
.f-col .head{color:#d6e5f7}
.f-rule{position:absolute;left:53px;width:1094px;border-top:1px solid rgba(255,255,255,.3)}
.badges{position:absolute;left:53px;top:302px;display:flex;gap:20px;font-size:14.5px}
.badges span{display:flex;align-items:center;gap:7px}
.social{position:absolute;left:893px;top:294px;display:flex;gap:9.5px}
.social i{width:33px;height:33px;border-radius:50%;background:rgba(255,255,255,.15);display:flex;align-items:center;justify-content:center}
.social i::after{content:"";width:13px;height:13px;border-radius:50%;background:var(--white)}
.copy{position:absolute;left:53px;top:372px;font-size:9.5px}
.legal{position:absolute;right:53px;top:369px;display:flex;gap:22px;font-size:13px}
.disclaimer{position:absolute;left:53px;top:410px;width:1094px;font-size:9.3px;line-height:11.5px;color:#e6efff}
</style>
</head>
<body>

<header class="nav">
  <div class="brand">MotorLane</div>
  <nav class="nav-links">
    <span>Search</span><span>Sell Your Car</span><span>Deals</span><span>Insurance</span><span>Research</span><span class="pro">♔ PRO</span>
  </nav>
  <div class="login">Log in</div>
  <svg class="menu" width="18" height="16" viewBox="0 0 18 16"><path d="M1 2h16M1 8h16M1 14h16" stroke="#374151" stroke-width="1.8"/></svg>
</header>

<section class="hero">
  <div class="hero-photo" role="img" aria-label="Close-up photo of a glossy blue sedan's front headlight and wheel under studio lighting"></div>
  <h1>CAR BUYING,<br>REVERSED</h1>
  <p>Find your next car. MotorLane<br>Experts negotiate the best price.</p>

  <form class="search-split" aria-label="Search by chat or by make and model">
    <div class="chat-pane">
      <div class="chat-text">I want a used 2022 Arden Sable with low mileage...</div>
      <svg class="chat-mic" width="12" height="16" viewBox="0 0 12 16"><rect x="3" y="1" width="6" height="9" rx="3" fill="none" stroke="#4b5563" stroke-width="1.4"/><path d="M1 7.5a5 5 0 0010 0M6 12.5V15" fill="none" stroke="#4b5563" stroke-width="1.4"/></svg>
      <div class="chat-send"><svg width="12" height="13" viewBox="0 0 12 13"><path d="M6 12V2M2 6l4-4 4 4" fill="none" stroke="#fff" stroke-width="1.8"/></svg></div>
    </div>
    <div class="manual-pane">
      <div class="field">Make<svg width="10" height="6" viewBox="0 0 10 6"><path d="M1 1l4 4 4-4" fill="none" stroke="#4b5563" stroke-width="1.4"/></svg></div>
      <div class="field">Model<svg width="10" height="6" viewBox="0 0 10 6"><path d="M1 1l4 4 4-4" fill="none" stroke="#4b5563" stroke-width="1.4"/></svg></div>
      <div class="go">Search</div>
    </div>
  </form>
</section>

<h2 class="title" style="top:780px">How MotorLane Works</h2>

<div class="step" style="top:860px">
  <svg width="50" height="48" viewBox="0 0 50 48"><rect x="6" y="8" width="34" height="34" rx="8" fill="none" stroke="#1a7fe8" stroke-width="4"/><rect x="30" y="2" width="16" height="16" fill="#fff"/><path d="M38 2l2.5 5.5L46 10l-5.5 2.5L38 18l-2.5-5.5L30 10l5.5-2.5z" fill="#1a7fe8"/></svg>
  <h3>1.&nbsp; Find Your Car</h3>
  <p>Search our inventory for the make, model, and year you want.</p>
</div>

<div class="step" style="top:1005px">
  <svg width="52" height="48" viewBox="0 0 52 48"><rect x="12" y="6" width="28" height="28" rx="7" transform="rotate(45 26 20) translate(0 4)" fill="none" stroke="#1a7fe8" stroke-width="4.5"/><path d="M18 24l8-8 8 8" fill="none" stroke="#1a7fe8" stroke-width="4"/></svg>
  <h3>2. Start MotorLane AI Negotiations</h3>
  <p>MotorLane makes dealers compete for you.</p>
</div>

<div class="step" style="top:1162px">
  <svg width="52" height="36" viewBox="0 0 52 36"><circle cx="18" cy="18" r="13" fill="none" stroke="#1a7fe8" stroke-width="4.5"/><circle cx="34" cy="18" r="13" fill="none" stroke="#1a7fe8" stroke-width="4.5"/></svg>
  <h3>3. Review Your Offers</h3>
  <p>Watch competing offers come in from multiple dealers.</p>
</div>

<div class="step" style="top:1288px">
  <svg width="52" height="50" viewBox="0 0 52 50"><path d="M6 30l5-11h20l5 11v12H6z" fill="none" stroke="#1a7fe8" stroke-width="4"/><circle cx="13" cy="35" r="2.5" fill="#1a7fe8"/><circle cx="29" cy="35" r="2.5" fill="#1a7fe8"/><path d="M30 4h14v14l-8 8-14-14z" fill="none" stroke="#1a7fe8" stroke-width="4"/><circle cx="39" cy="10" r="2" fill="#1a7fe8"/></svg>
  <h3>4. Choose Your Deal</h3>
  <p>Pick the winning offer and drive it home.</p>
</div>

<div class="btn" style="top:1425px">Watch Dealers Compete</div>

<h2 class="title" style="top:1501px">Today's Deals</h2>

<article class="card" style="left:55px">
  <div class="card-photo" role="img" aria-label="Studio photo of a black sedan on a light grey turntable"></div>
  <div class="fav"><svg width="12" height="11" viewBox="0 0 12 11"><path d="M6 10L1.5 5.5A2.6 2.6 0 016 2a2.6 2.6 0 014.5 3.5z" fill="none" stroke="#fff" stroke-width="1.3"/></svg></div>
  <div class="card-body">
    <h4>Used 2019 Nordhal R60</h4><div class="trim">R4 Touring</div>
    <div class="price-row"><span class="price">$20 312</span><span class="miles">◠ 78 225 mi</span></div>
    <div class="est">Est. $303/mo*</div><span class="tag">5 days on market</span>
    <div class="swatch"><span class="dot"></span>White</div>
    <div class="swatch" style="margin-top:7px"><span class="dot" style="background:#374151;border-color:#374151"></span>Gray</div>
  </div>
  <div class="card-foot"><svg width="11" height="13" viewBox="0 0 11 13"><path d="M5.5 12S1 7.5 1 5a4.5 4.5 0 019 0c0 2.5-4.5 7-4.5 7z" fill="none" stroke="#4b5563" stroke-width="1.2"/><circle cx="5.5" cy="5" r="1.5" fill="none" stroke="#4b5563"/></svg>SCHAUMBURG, IL</div>
</article>

<article class="card" style="left:331px">
  <div class="card-photo" role="img" aria-label="Studio photo of a black sedan on a light grey turntable"></div>
  <div class="fav"><svg width="12" height="11" viewBox="0 0 12 11"><path d="M6 10L1.5 5.5A2.6 2.6 0 016 2a2.6 2.6 0 014.5 3.5z" fill="none" stroke="#fff" stroke-width="1.3"/></svg></div>
  <div class="card-body">
    <h4>Used 2019 Nordhal R60</h4><div class="trim">R4 Touring</div>
    <div class="price-row"><span class="price">$20 312</span><span class="miles">◠ 78 225 mi</span></div>
    <div class="est">Est. $303/mo*</div><span class="tag">5 days on market</span>
  </div>
  <div class="card-foot"><svg width="11" height="13" viewBox="0 0 11 13"><path d="M5.5 12S1 7.5 1 5a4.5 4.5 0 019 0c0 2.5-4.5 7-4.5 7z" fill="none" stroke="#4b5563" stroke-width="1.2"/><circle cx="5.5" cy="5" r="1.5" fill="none" stroke="#4b5563"/></svg>SCHAUMBURG, IL</div>
</article>

<article class="card" style="left:606px">
  <div class="card-photo" role="img" aria-label="Studio photo of a black sedan on a light grey turntable"></div>
  <div class="fav"><svg width="12" height="11" viewBox="0 0 12 11"><path d="M6 10L1.5 5.5A2.6 2.6 0 016 2a2.6 2.6 0 014.5 3.5z" fill="none" stroke="#fff" stroke-width="1.3"/></svg></div>
  <div class="card-body">
    <h4>Used 2019 Nordhal R60</h4><div class="trim">R4 Touring</div>
    <div class="price-row"><span class="price">$20 312</span><span class="miles">◠ 78 225 mi</span></div>
    <div class="est">Est. $303/mo*</div><span class="tag">5 days on market</span>
  </div>
  <div class="card-foot"><svg width="11" height="13" viewBox="0 0 11 13"><path d="M5.5 12S1 7.5 1 5a4.5 4.5 0 019 0c0 2.5-4.5 7-4.5 7z" fill="none" stroke="#4b5563" stroke-width="1.2"/><circle cx="5.5" cy="5" r="1.5" fill="none" stroke="#4b5563"/></svg>SCHAUMBURG, IL</div>
</article>

<article class="card" style="left:882px">
  <div class="card-photo" role="img" aria-label="Studio photo of a black sedan on a light grey turntable"></div>
  <div class="fav"><svg width="12" height="11" viewBox="0 0 12 11"><path d="M6 10L1.5 5.5A2.6 2.6 0 016 2a2.6 2.6 0 014.5 3.5z" fill="none" stroke="#fff" stroke-width="1.3"/></svg></div>
  <div class="card-body">
    <h4>Used 2019 Nordhal R60</h4><div class="trim">R4 Touring</div>
    <div class="price-row"><span class="price">$20 312</span><span class="miles">◠ 78 225 mi</span></div>
    <div class="est">Est. $303/mo*</div><span class="tag">5 days on market</span>
  </div>
  <div class="card-foot"><svg width="11" height="13" viewBox="0 0 11 13"><path d="M5.5 12S1 7.5 1 5a4.5 4.5 0 019 0c0 2.5-4.5 7-4.5 7z" fill="none" stroke="#4b5563" stroke-width="1.2"/><circle cx="5.5" cy="5" r="1.5" fill="none" stroke="#4b5563"/></svg>SCHAUMBURG, IL</div>
</article>

<div class="btn" style="top:2114px">View All Deals</div>

<h2 class="title" style="top:2174px">The Old Way vs The MotorLane Way</h2>

<div class="compare">
  <div class="abs" style="left:229px;top:2244px">
    <h3>The Old Way</h3>
    <ul>
      <li>You visit dealership after dealership</li>
      <li>Every salesperson has an agenda</li>
      <li>Inconsistent pricing and hidden fees</li>
      <li>Hours of back-and-forth negotiation</li>
      <li>You leave wondering if you got played</li>
      <li>Pressure to decide on dealer's timeline</li>
    </ul>
  </div>
  <div class="abs ours" style="left:578px;top:2244px">
    <h3>MotorLane</h3>
    <ul>
      <li>Dealers come to you</li>
      <li>MotorLane works for buyers, not dealers</li>
      <li>Transparent pricing from competing dealers</li>
      <li>Built-in negotiation handles it</li>
      <li>You leave knowing you got the best deal</li>
      <li>Your timeline. Your decision</li>
    </ul>
  </div>
</div>

<h2 class="title" style="top:2470px">FAQ</h2>

<div class="faq" style="top:2529px">
  <h4>Does MotorLane cost anything to use?<span>+</span></h4>
  <p>MotorLane marketplace is completely free for browsers. If you're looking to buy and want to utilize our negotiation technology, we have multiple upgrade packages available.</p>
</div>
<div class="faq" style="top:2630px"><h4>Do I still have to negotiate with dealerships?<span>+</span></h4></div>
<div class="faq" style="top:2681px"><h4>How do I know the price is fair?<span>+</span></h4></div>
<div class="faq-end"></div>

<div class="btn" style="top:2763px">View All FAQs</div>

<h2 class="title" style="top:2836px">Ready to find your next car?</h2>
<div class="search-pill">I want a new Kestrel, black SUV...
  <svg style="position:absolute;right:12px;top:7px" width="28" height="14" viewBox="0 0 28 14"><rect x="3" y="1" width="5" height="8" rx="2.5" fill="none" stroke="#fff" stroke-width="1.4"/><path d="M1 7a4.5 4.5 0 009 0M5.5 11.5V13M22 13V2M18 6l4-4 4 4" fill="none" stroke="#fff" stroke-width="1.5"/></svg>
</div>

<footer class="footer">
  <div class="f-brand">MotorLane</div>
  <div class="f-tag">The smarter way to buy your next car</div>
  <div class="f-contact" style="top:160px"><svg width="16" height="12" viewBox="0 0 16 12"><rect x="1" y="1" width="14" height="10" rx="1.5" fill="none" stroke="#fff" stroke-width="1.4"/><path d="M1.5 2l6.5 5 6.5-5" fill="none" stroke="#fff" stroke-width="1.4"/></svg>hello@motorlane.net</div>
  <div class="f-contact" style="top:191px"><svg width="14" height="16" viewBox="0 0 14 16"><path d="M7 15S1.5 9.5 1.5 6a5.5 5.5 0 0111 0C12.5 9.5 7 15 7 15z" fill="none" stroke="#fff" stroke-width="1.4"/><circle cx="7" cy="6" r="2" fill="none" stroke="#fff" stroke-width="1.4"/></svg>Chicago, IL</div>

  <div class="f-col" style="left:428px"><div class="head">For Buyers</div><div style="margin-top:4px">Search</div><div>Daily Deals</div><div>How It Works</div><div>Car Value Calculator</div></div>
  <div class="f-col" style="left:614px"><div class="head">Resources</div><div style="margin-top:4px">Guides</div><div>Research</div><div>FAQ</div></div>
  <div class="f-col" style="left:799px"><div class="head">Company</div><div style="margin-top:4px">About Us</div><div>Contact</div><div>Affiliate Program</div></div>

  <div class="f-rule" style="top:254px"></div>
  <div class="badges">
    <span><svg width="14" height="16" viewBox="0 0 14 16"><path d="M7 1l5.5 2v5c0 3.5-2.5 5.5-5.5 7-3-1.5-5.5-3.5-5.5-7V3z" fill="none" stroke="#fff" stroke-width="1.4"/></svg>SSL Secured</span>
    <span><svg width="14" height="16" viewBox="0 0 14 16"><circle cx="7" cy="6" r="4.5" fill="none" stroke="#fff" stroke-width="1.4"/><path d="M4.5 10l-1 5 3.5-2 3.5 2-1-5" fill="none" stroke="#fff" stroke-width="1.4"/></svg>Top Rated</span>
    <span><svg width="16" height="16" viewBox="0 0 16 16"><circle cx="8" cy="8" r="6.5" fill="none" stroke="#fff" stroke-width="1.4"/><path d="M5 8l2 2 4-4" fill="none" stroke="#fff" stroke-width="1.4"/></svg>Verified Dealers</span>
  </div>
  <div class="social" aria-label="Social links"><i></i><i></i><i></i><i></i><i></i><i></i></div>
  <div class="f-rule" style="top:345px"></div>
  <div class="copy">© 2026 MotorLane. All rights reserved.</div>
  <div class="legal"><span>Report Problem</span><span>Terms &amp; Conditions</span><span>Privacy Policy</span></div>
  <p class="disclaimer">MotorLane operates independently and is not sponsored, endorsed, affiliated with, or authorized by any automaker or trademark owner. All listing details, including vehicle specs, photos and pricing, come from sellers and outside data sources. Brand names and vehicle images appear only to identify and describe vehicles. MotorLane makes no promise about accuracy or completeness. All prices are shown in U.S. Dollars. Buyers should confirm availability, price, vehicle condition and all sale terms directly with the seller.</p>
</footer>

</body>
</html>
```